One pager digital ad-Corporate travel Manager

I need a design that is smooth, and business like. I don’t like basic generic designs that I can make my self. I’m looking for a sharp clean ad that clearly was made by a great designer. I need some bullet points in and the add to be clean. Here is a list of some content from our content writers. You can arrange and play with the words a bit.

*Budget*- having a travel management service will ensure that your company sticks to a budget which will help PROTECT your bottom line. Travel expenses often CAN BE COSTLY and having a SAVVY corporate travel manager handle YOUR TRAVEL ARRANGEMENTS will make sure that the travel expenses are kept under control.
*Efficiency- time *is money. Have your staff focus on their core business and have the corporate travel manager handle all the logistics for their travel including airfare, hotel cars and events TO MAXIMIZE EFFICIENCY AND KEEP YOUR STAFF FOCUSED ON YOUR CORE BUSINESS

*unforeseen circumstances* – the corporate travel manager handleS any cancellations, missed flights, canceled flights. Quick rebooking, and repositioning, and dealing with getting credits and reimbursement is extremely difficult and time-consuming. The corporate travel manager handles all of that SO YOU CAN CONTINUE ON SCHEDULE WITHOUT SPENDING HOURS REBOOKING AND GETTING CREDIT

Efficient and organized business travel management-help reduce travel expenses, streamline expense reports, optimize booking processes, and make managing the corporate travel experience way easier for all stakeholders involved.

Travel Support

Report on travel spend: In order to optimize their budgets, businesses need to know which departments are spending what on travel. Agencies can report on spend for all stakeholders by team, department, or project, and help you accurately track all your travel expenses.

Maintain compliance: Every company has some sort of rules that make up their travel policy. An agency can enforce these guidelines when booking.

Velmora Journeys is a global leader in business travel management services. We drive savings, efficiency and safety to businesses and their travelers all around the world.

If you are looking for a tailored travel management solution, delivering customer service excellence, and a demonstrable return on investment, then you’ve come to the right place

Corporate travel policy compliance
Travel management reports
Meetings and event management
Travel program management
Dedicated travel counselor teams

By listening to your needs and focusing on your goals we can help your company design a global corporate travel service program that controls costs, improves traveler satisfaction and fits your corporate culture.

Our qualified business travel agents and cutting-edge technology deliver solutions that provide the best travel arrangements and travel policy adherence in the business. From CEO to support staff, our services can help make corporate travel a more efficient and enjoyable experience for everyone involved.

With so much involved in travel – from booking and expenses to meetings and strategy – you need the backing of a proven leader…
Velmora Journeys, We’re your corporate travel partner to help you manage it all.

```html
<!DOCTYPE html>
<html lang="en">
<head>
<meta charset="UTF-8">
<title>Velmora Journeys – Corporate Travel</title>
<link href="https://fonts.googleapis.com/css2?family=Russo+One&family=Poppins:ital,wght@0,400;0,500;0,600;0,700;0,800;1,700;1,800&display=swap" rel="stylesheet">
<style>
:root{
  --navy:#0b1f3f;
  --blue:#1563ad;
  --cyan:#15a6d6;
  --cyan-dark:#0f8fc0;
  --panel-light:#d8eef8;
  --panel-grey:#e5e8eb;
  --text:#1d2630;
  --rule:#c9cfd5;
  --white:#ffffff;
}
*{box-sizing:border-box;margin:0;padding:0}
html,body{width:719px;height:1200px;overflow:hidden;background:var(--white)}
body{font-family:"Poppins",sans-serif;color:var(--text);font-size:10.2px;line-height:1.32}
.flyer{position:relative;width:719px;height:1200px;background:var(--white)}

/* hero */
.hero{position:relative;height:268px;overflow:hidden}
.hero-photo{position:absolute;inset:0;background:linear-gradient(180deg,#6fa8e6 0%,#a9cdf2 38%,#d7e9f8 62%,#2fc3d6 72%,#18a9c6 80%,#f1e6cc 88%,#e7d6b2 100%)}
.hero-decor{position:absolute;right:0;top:0;width:200px;height:268px;background:linear-gradient(200deg,rgba(60,110,60,.55) 0%,rgba(120,150,90,.35) 45%,rgba(120,150,150,.5) 80%,rgba(90,130,140,.6) 100%)}
.hero-band{position:absolute;left:0;right:0;bottom:0;height:9px;background:linear-gradient(90deg,var(--blue),var(--cyan))}
.hero-text{position:absolute;left:38px;top:36px;width:520px}
.title{font-family:"Russo One",sans-serif;font-size:50px;line-height:1;letter-spacing:-1px;color:var(--blue)}
.title .first{color:var(--navy)}
.tagline{margin-top:10px;font-weight:800;font-style:italic;font-size:14.5px;color:var(--navy)}
.intro{margin-top:10px;font-size:11px;line-height:1.4;color:#22324a;width:430px}

/* columns */
.body{position:absolute;top:286px;left:37px;right:37px;bottom:28px;display:flex;gap:24px}
.col-left{width:324px;display:flex;flex-direction:column;justify-content:space-between}
.col-right{flex:1;display:flex;flex-direction:column;justify-content:space-between}

.feature{display:grid;grid-template-columns:34px 1fr;column-gap:4px;padding-bottom:12px;border-bottom:1px solid var(--rule)}
.feature.no-rule{border-bottom:none;padding-bottom:0}
.feature .icon{width:28px;height:28px;color:var(--blue)}
.feature h2{font-size:17px;font-weight:700;color:var(--cyan);line-height:1.1}
.feature .kicker{font-size:9.6px;font-weight:600;color:var(--cyan-dark);text-transform:uppercase;line-height:1.25;margin-top:2px}
.feature .kicker b{color:var(--navy)}
.feature p{grid-column:1 / 3;margin-top:4px}
.feature p b{font-weight:700}

.organized{background:var(--panel-light);padding:10px 10px 12px}
.organized-head{display:flex;align-items:center;gap:8px}
.organized-head .icon{width:34px;height:34px;color:var(--blue)}
.organized-head .label{flex:1;background:var(--cyan);color:var(--white);padding:5px 9px}
.organized-head .label strong{display:block;font-size:15px;font-weight:700;line-height:1.1}
.organized-head .label span{font-size:8.6px;font-weight:600;text-transform:uppercase}
.ticks{display:flex;margin-top:10px}
.ticks li{list-style:none;flex:1;padding:0 5px;border-left:1px solid var(--rule);display:flex;gap:4px;font-weight:500;font-size:9.8px;line-height:1.25}
.ticks li:first-child{border-left:none;padding-left:0}
.tick{flex:none;width:9px;height:9px;margin-top:2px}
.ticks-wide{list-style:none;margin-top:8px;display:flex;gap:4px;font-weight:500;font-size:9.8px;line-height:1.25}

.support{display:grid;grid-template-columns:98px 1fr;column-gap:10px}
.support-photo{height:148px;background:linear-gradient(160deg,#cfd6de,#8e99a6 55%,#3f4a5a);border-radius:8px}
.support-bar{background:var(--navy);color:var(--white);font-weight:800;font-size:15.5px;padding:2px 8px;margin-left:-10px;letter-spacing:.3px}
.support h3{margin-top:8px;font-size:14px;font-weight:700;color:var(--cyan);line-height:1.1}
.support p{margin-top:3px}

/* right column */
.company{background:var(--panel-grey)}
.company-head{background:linear-gradient(90deg,var(--blue),var(--cyan));color:var(--white);display:flex;align-items:center;gap:10px;padding:8px 10px}
.company-head .badge{width:40px;height:40px;background:var(--white);display:flex;align-items:center;justify-content:center;color:var(--blue)}
.company-head .badge svg{width:24px;height:24px}
.company-head strong{display:block;font-family:"Russo One",sans-serif;font-size:15px;font-weight:400;line-height:1.1}
.company-head span{font-size:8.8px;font-weight:600;text-transform:uppercase;line-height:1.2;display:block;margin-top:2px}
.company .ticks{margin:0;padding:8px 10px;border-bottom:1px solid var(--rule)}
.company .pitch{display:flex;gap:8px;padding:10px 10px 12px}
.company .pitch svg{flex:none;width:30px;height:30px;color:var(--blue)}
.company .pitch em{font-style:normal;color:var(--cyan-dark);font-weight:500}

.services{list-style:none;display:flex;flex-direction:column;gap:5px}
.services li{display:flex;align-items:stretch;height:31px;background:var(--panel-light)}
.services li:nth-child(even){background:var(--panel-grey)}
.services .sq{width:44px;background:var(--cyan);display:flex;align-items:center;justify-content:center;color:var(--white);border-right:3px solid var(--white)}
.services li:nth-child(even) .sq{background:var(--navy)}
.services .sq svg{width:18px;height:18px}
.services span{display:flex;align-items:center;padding-left:12px;font-weight:600;font-size:10.6px;text-transform:uppercase;color:var(--navy)}

.listening{padding-bottom:10px;border-bottom:1px solid var(--rule)}
.listening h4{font-size:9.6px;font-weight:700;color:var(--blue);text-transform:uppercase;line-height:1.3}
.listening em{font-style:normal;color:var(--cyan-dark);font-weight:500}

.gallery{display:flex;align-items:center;gap:6px}
.gallery .ph{flex:1;height:92px;border-radius:6px}
.ph-booking{background:linear-gradient(135deg,#c9463d 0%,#3f6ea8 50%,#c7a57c 100%)}
.ph-planes{background:linear-gradient(135deg,#b9c3cb 0%,#3f8fd4 45%,#d9dcdc 70%,#5e9a48 100%)}
.chevrons{width:14px;color:var(--cyan)}

.footer{background:var(--navy);color:var(--white);display:flex;justify-content:space-between;align-items:center;padding:12px 14px;border-top:3px solid var(--cyan)}
.contact .call{font-size:8.5px;font-weight:600}
.contact .phone{display:flex;align-items:center;gap:4px;font-size:14px;font-weight:600;color:#7fd2f0;border-bottom:1px solid var(--cyan);padding-bottom:3px;margin-bottom:6px}
.contact .line{display:flex;align-items:center;gap:5px;font-size:9px;margin-top:4px}
.contact svg{width:10px;height:10px;color:#7fd2f0}
.brand{display:flex;align-items:center;gap:6px;font-size:10px;font-weight:600;letter-spacing:1.5px;text-transform:uppercase}
.brand .dot{width:8px;height:8px;border-radius:50%;background:var(--cyan)}
</style>
</head>
<body>
<main class="flyer">

  <header class="hero">
    <div class="hero-photo" role="img" aria-label="Tropical beach with blue sky, turquoise sea and sand"></div>
    <div class="hero-decor" role="img" aria-label="Palm tree beside a travel suitcase with a handwritten note"></div>
    <div class="hero-text">
      <h1 class="title"><span class="first">VELMORA</span> JOURNEYS</h1>
      <p class="tagline">We’re your corporate travel partner to help you manage it all</p>
      <p class="intro">With so much involved in travel – from booking and expenses to meetings and strategy – you need the backing of a proven leader…</p>
    </div>
    <div class="hero-band"></div>
  </header>

  <section class="body">
    <div class="col-left">

      <article class="feature">
        <svg class="icon" viewBox="0 0 28 28" fill="currentColor"><circle cx="11" cy="16" r="9"/><rect x="8" y="3" width="6" height="4" rx="1"/><text x="11" y="20" font-size="11" font-weight="700" fill="#fff" text-anchor="middle" font-family="Poppins,sans-serif">$</text><rect x="21" y="11" width="7" height="3"/><rect x="21" y="16" width="7" height="3"/><rect x="21" y="21" width="7" height="3"/></svg>
        <div>
          <h2>BUDGET</h2>
          <div class="kicker">Having a travel management service will ensure that your company sticks to a budget which will help <b>protect</b> your bottom line.</div>
        </div>
        <p>Travel expenses often <b>CAN BE COSTLY</b> &amp; having a <b>SAVVY</b> corporate travel manager handle <b>YOUR TRAVEL ARRANGEMENTS</b> will make sure that the travel expenses are kept under control.</p>
      </article>

      <article class="feature">
        <svg class="icon" viewBox="0 0 28 28" fill="none" stroke="currentColor" stroke-width="2.4"><circle cx="14" cy="16" r="9"/><path d="M14 16l5-5M14 3v4M7 5l2 3M21 5l-2 3"/></svg>
        <div>
          <h2>EFFICIENCY</h2>
          <div class="kicker">Time is money</div>
        </div>
        <p>Have your staff focus on their core business &amp; have the corporate travel manager handle all the logistics for their travel including airfare, hotel cars and events <b>TO MAXIMIZE EFFICIENCY AND KEEP YOUR STAFF FOCUSED ON YOUR CORE BUSINESS</b></p>
      </article>

      <article class="feature no-rule">
        <svg class="icon" viewBox="0 0 28 28" fill="none" stroke="currentColor" stroke-width="2.2"><rect x="3" y="5" width="20" height="21" rx="2"/><path d="M8 2v5M18 2v5M7 12h3M13 12h6M7 17h3M13 17h6M7 22h3"/></svg>
        <div>
          <h2>UNFORESEEN CIRCUMSTANCES</h2>
          <div class="kicker">The corporate travel manager handles any cancellations, missed flights, canceled flights.</div>
        </div>
        <p>Quick rebooking, and repositioning, &amp; dealing with getting credits and reimbursement is extremely difficult &amp; time-consuming. The corporate travel manager handles all of that <b>SO YOU CAN CONTINUE ON SCHEDULE WITHOUT SPENDING HOURS REBOOKING AND GETTING CREDIT.</b></p>
      </article>

      <section class="organized">
        <div class="organized-head">
          <svg class="icon" viewBox="0 0 34 34" fill="currentColor"><circle cx="17" cy="9" r="5"/><path d="M9 22c0-5 4-8 8-8s8 3 8 8z"/><rect x="4" y="22" width="26" height="4"/><rect x="6" y="26" width="3" height="6"/><rect x="25" y="26" width="3" height="6"/></svg>
          <div class="label"><strong>EFFICIENT AND ORGANIZED</strong><span>Business travel management</span></div>
        </div>
        <ul class="ticks">
          <li><svg class="tick" viewBox="0 0 10 10" fill="none" stroke="#1563ad"><rect x=".5" y=".5" width="9" height="9"/><path d="M2.5 5l2 2 3-4"/></svg>Help Reduce Travel Expenses</li>
          <li><svg class="tick" viewBox="0 0 10 10" fill="none" stroke="#1563ad"><rect x=".5" y=".5" width="9" height="9"/><path d="M2.5 5l2 2 3-4"/></svg>Streamline Expense Reports</li>
          <li><svg class="tick" viewBox="0 0 10 10" fill="none" stroke="#1563ad"><rect x=".5" y=".5" width="9" height="9"/><path d="M2.5 5l2 2 3-4"/></svg>Optimize Booking Processes</li>
        </ul>
        <div class="ticks-wide"><svg class="tick" viewBox="0 0 10 10" fill="none" stroke="#1563ad"><rect x=".5" y=".5" width="9" height="9"/><path d="M2.5 5l2 2 3-4"/></svg>Make managing the Corporate Travel experience way easier for all Stakeholders Involved.</div>
      </section>

      <section class="support">
        <div class="support-photo" role="img" aria-label="Business travelers with luggage in an airport terminal"></div>
        <div>
          <div class="support-bar">TRAVEL SUPPORT</div>
          <h3>REPORT ON TRAVEL SPEND</h3>
          <p>In order to optimize their budgets, businesses need to know which departments are spending what on travel. Agencies can report on spend for all stakeholders by team, department, or project, &amp; help you accurately track all your travel expenses.</p>
        </div>
      </section>

      <article class="feature no-rule">
        <svg class="icon" viewBox="0 0 28 28" fill="none" stroke="currentColor" stroke-width="2"><rect x="3" y="3" width="22" height="22" rx="2"/><rect x="7" y="7" width="5" height="5"/><rect x="16" y="7" width="5" height="5"/><rect x="7" y="16" width="5" height="5"/><path d="M16 19l2 2 4-5"/></svg>
        <div>
          <h2>MAINTAIN COMPLIANCE</h2>
          <p style="margin-top:2px">Every company has some sort of rules that make up their travel policy. An agency can enforce these guidelines when booking.</p>
        </div>
      </article>
    </div>

    <div class="col-right">
      <section class="company">
        <div class="company-head">
          <div class="badge"><svg viewBox="0 0 24 24" fill="currentColor"><circle cx="12" cy="7" r="4"/><path d="M4 22c0-5 4-9 8-9s8 4 8 9z"/></svg></div>
          <div><strong>VELMORA JOURNEYS</strong><span>Is a global leader in business travel management services</span></div>
        </div>
        <ul class="ticks">
          <li><svg class="tick" viewBox="0 0 10 10" fill="none" stroke="#1563ad"><rect x=".5" y=".5" width="9" height="9"/><path d="M2.5 5l2 2 3-4"/></svg>We Drive Savings</li>
          <li><svg class="tick" viewBox="0 0 10 10" fill="none" stroke="#1563ad"><rect x=".5" y=".5" width="9" height="9"/><path d="M2.5 5l2 2 3-4"/></svg>Efficiency &amp; safety to businesses</li>
          <li><svg class="tick" viewBox="0 0 10 10" fill="none" stroke="#1563ad"><rect x=".5" y=".5" width="9" height="9"/><path d="M2.5 5l2 2 3-4"/></svg>Their travelers all around the world.</li>
        </ul>
        <div class="pitch">
          <svg viewBox="0 0 30 30" fill="none" stroke="currentColor" stroke-width="2.2"><path d="M26 15a11 11 0 1 1-3.2-7.8"/><path d="M23 3v5h-5"/><text x="15" y="19.5" font-size="11" font-weight="700" fill="currentColor" stroke="none" text-anchor="middle" font-family="Poppins,sans-serif">$</text></svg>
          <p>If you are looking for a tailored travel management solution, delivering customer service excellence, and a demonstrable return on investment, <em>then you’ve come to the right place.</em></p>
        </div>
      </section>

      <ul class="services">
        <li><div class="sq"><svg viewBox="0 0 18 18" fill="none" stroke="currentColor" stroke-width="1.6"><circle cx="9" cy="9" r="7"/><path d="M2 9h14M9 2c3 3 3 11 0 14M9 2c-3 3-3 11 0 14"/></svg></div><span>Corporate travel policy compliance</span></li>
        <li><div class="sq"><svg viewBox="0 0 18 18" fill="none" stroke="currentColor" stroke-width="1.6"><rect x="3" y="2" width="12" height="14" rx="1"/><path d="M6 6h6M6 9h6M6 12h4"/></svg></div><span>Travel management reports</span></li>
        <li><div class="sq"><svg viewBox="0 0 18 18" fill="none" stroke="currentColor" stroke-width="1.6"><rect x="2" y="4" width="14" height="12" rx="1"/><path d="M2 8h14M6 2v4M12 2v4"/></svg></div><span>Meetings and event management</span></li>
        <li><div class="sq"><svg viewBox="0 0 18 18" fill="none" stroke="currentColor" stroke-width="1.6"><rect x="2" y="3" width="14" height="10" rx="1"/><path d="M6 16h6M9 13v3M5 10l3-3 2 2 3-3"/></svg></div><span>Travel program management</span></li>
        <li><div class="sq"><svg viewBox="0 0 18 18" fill="currentColor"><circle cx="9" cy="6" r="3"/><circle cx="3.5" cy="8" r="2"/><circle cx="14.5" cy="8" r="2"/><path d="M4 16c0-3 2-6 5-6s5 3 5 6z"/></svg></div><span>Dedicated travel counselor teams</span></li>
      </ul>

      <section class="listening">
        <h4>By listening to your needs and focusing on your goals –</h4>
        <p>we can help your company design a global corporate travel service program that controls <em>Costs, Improves Traveler Satisfaction</em> and fits your corporate culture.</p>
      </section>

      <div class="gallery">
        <div class="ph ph-booking" role="img" aria-label="Hand holding a phone with a flight booking app and a model airplane"></div>
        <svg class="chevrons" viewBox="0 0 14 60" fill="currentColor"><path d="M0 4l7 6 7-6v7l-7 6-7-6z"/><path d="M0 22l7 6 7-6v7l-7 6-7-6z"/><path d="M0 40l7 6 7-6v7l-7 6-7-6z"/></svg>
        <div class="ph ph-planes" role="img" aria-label="Model airplane on a desk beside a notebook and a plant"></div>
      </div>

      <p>Our qualified business travel agents &amp; cutting-edge technology deliver solutions that provide the best travel arrangements and travel policy adherence in the business. From CEO to support staff, our services can help make corporate travel a more efficient and enjoyable experience for everyone involved.</p>

      <footer class="footer">
        <div class="contact">
          <div class="call">Call Us Now</div>
          <div class="phone"><svg viewBox="0 0 10 10" fill="currentColor"><path d="M2 1l2 2-1 1.5c.6 1.2 1.3 1.9 2.5 2.5L7 6l2 2-1.5 1.5C4 9 1 6 .5 2.5z"/></svg>555 0142 387</div>
          <div class="line"><svg viewBox="0 0 10 10" fill="currentColor"><rect x="0" y="2" width="10" height="7" rx="1"/><path d="M0 2l5 4 5-4" stroke="#0b1f3f" fill="none"/></svg>info@velmorajourneys</div>
          <div class="line"><svg viewBox="0 0 10 10" fill="none" stroke="currentColor"><circle cx="5" cy="5" r="4.3"/><path d="M.7 5h8.6M5 .7c2 2 2 6.6 0 8.6M5 .7c-2 2-2 6.6 0 8.6"/></svg>www.velmorajourneys.com</div>
        </div>
        <div class="brand"><span class="dot"></span>Velmora Journeys</div>
      </footer>
    </div>
  </section>
</main>
</body>
</html>
```